Bright Meadow Dental Lab - Presentation Folder Design

1. We are a dental lab providing a full range of dental products to restore and enhance the natural beauty of the patients’ smiles. We provide fixed restorations (Full-Contour Solid Zirconia, KTR o.lux, Nimbo Core, Full Cast, PFM, Temporary Crowns, Diagnostic Wax-Ups and Study Models), implant restorations (Single and Multi Tooth Restorations, Zirconia Prosthesis, Full Arch Hybrid Prosthesis), and
removable restorations (Dentures and Partials, PliaTek, Sorvent).
2. The target market are dentists, oral surgeons, implant manufacturers, and etc. We are not targeting patients.
3. Design specifics - no specifics, but I have provided our logo for reference if needed

Target Market(s)

Dentists, Oral Surgeons, implant manufacturers

Industry/Entity Type

Dental

Requirements
Must have
• Name - Bright Meadow Dental Lab, address - 4126 Larkspur Ln, Suite 310, Larkton, VA 22190, office number - 703-555-0142, fax number - 703-555-0143, email - info@bmdentalstudio.example

```html
<!DOCTYPE html>
<html lang="en">
<head>
<meta charset="utf-8">
<title>Bright Meadow Dental Lab – Presentation Folder</title>
<link href="https://fonts.googleapis.com/css2?family=Montserrat:wght@400;500;600;700;800&display=swap" rel="stylesheet">
<style>
  :root {
    --brand-blue: #3a44a3;
    --brand-deep: #2b3384;
    --brand-lavender: #aeb2e3;
    --paper-light: #ffffff;
    --paper-shade: #d6d7dc;
    --ink-grey: #4a4a52;
    --title-grey: #cfd0d4;
    --canvas-bg: #bfbfc2;
    --disc-teal: #2f7486;
    --card-blue: #4d57b2;
  }
  * { box-sizing: border-box; margin: 0; padding: 0; }
  html, body { width: 913px; height: 1200px; overflow: hidden; background: var(--canvas-bg); }
  body { position: relative; font-family: "Montserrat", sans-serif; }

  .spread { position: absolute; left: 26px; width: 860px; height: 560px; display: flex; box-shadow: 0 8px 22px rgba(0,0,0,.25); }
  .spread--outside { top: 20px; }
  .spread--inside { top: 620px; }
  .page { position: relative; width: 430px; height: 560px; overflow: hidden; }
  .page svg.page-art { position: absolute; inset: 0; width: 430px; height: 560px; }
  .page--back, .page--inside-left { background: linear-gradient(160deg, var(--paper-light) 20%, var(--paper-shade) 100%); }
  .page--front, .page--inside-right { background: linear-gradient(200deg, var(--paper-light) 25%, var(--paper-shade) 100%); }

  .wordmark { position: absolute; left: 0; right: 0; text-align: center; color: var(--brand-blue); font-weight: 700; letter-spacing: 1px; line-height: 1.1; }
  .wordmark .dot { display: inline-block; width: .45em; height: .45em; border-radius: 50%; background: var(--brand-blue); vertical-align: middle; margin-right: .3em; }
  .wordmark--white { color: #fff; }
  .wordmark--front { top: 40px; font-size: 26px; }
  .wordmark--inside-left { top: 230px; font-size: 30px; }
  .wordmark--inside-right { top: 190px; font-size: 30px; }
  .wordmark__line2 { font-size: .65em; }

  /* back cover */
  .quote { position: absolute; left: 40px; right: 40px; top: 40px; text-align: center; color: var(--ink-grey); }
  .quote__mark { display: flex; align-items: center; gap: 14px; font-size: 70px; font-weight: 800; color: #c9c9ce; line-height: .7; height: 40px; }
  .quote__mark::before, .quote__mark::after { content: ""; flex: 1; height: 1px; background: #b5b5bb; }
  .quote__text { margin-top: 14px; font-size: 13px; line-height: 1.35; }
  .quote__author { margin-top: 14px; font-size: 13px; font-weight: 700; color: var(--brand-blue); }
  .back-footer { position: absolute; left: 0; right: 0; bottom: 26px; display: flex; align-items: center; padding: 0 24px; color: #fff; }
  .back-footer .wordmark { position: static; width: 120px; font-size: 13px; text-align: left; }
  .back-footer__divider { width: 1px; height: 58px; background: rgba(255,255,255,.7); margin: 0 16px; }
  .contact { font-size: 8.5px; line-height: 1.5; }
  .contact__name { font-size: 10px; font-weight: 700; }

  /* front cover */
  .title { position: absolute; left: 60px; top: 425px; }
  .title__main { font-size: 35px; font-weight: 800; color: var(--brand-blue); letter-spacing: .5px; }
  .title__sub { font-size: 35px; font-weight: 800; color: var(--title-grey); margin-top: -14px; letter-spacing: .5px; }
  .url-tab { position: absolute; right: 24px; bottom: 8px; width: 270px; height: 30px; background: var(--brand-blue); border-radius: 14px 0 0 0; color: #fff; font-size: 10px; letter-spacing: 1px; font-weight: 500; display: flex; align-items: center; justify-content: center; white-space: nowrap; }
  .front-baseline { position: absolute; left: 0; right: 0; bottom: 0; height: 8px; background: var(--brand-blue); }

  /* inside */
  .disc-label { position: absolute; left: 120px; top: 384px; width: 140px; font-size: 10px; }
  .business-card { position: absolute; left: 120px; top: 448px; width: 190px; height: 88px; background: var(--card-blue); border-top: 3px solid #fff; border-bottom: 3px solid #fff; color: #fff; text-align: center; padding-top: 7px; }
  .business-card .wordmark { position: static; font-size: 9px; }
  .business-card .contact { font-size: 5.5px; line-height: 1.45; margin-top: 4px; }
  .business-card .contact__name { font-size: 6.5px; }
</style>
</head>
<body>

<section class="spread spread--outside">
  <div class="page page--back">
    <svg class="page-art" viewBox="0 0 430 560">
      <defs>
        <linearGradient id="photoBack" x1="0" y1="0" x2="1" y2="1">
          <stop offset="0" stop-color="#e7e9ee"/>
          <stop offset=".6" stop-color="#8fb6dc"/>
          <stop offset="1" stop-color="#5aa0d8"/>
        </linearGradient>
      </defs>
      <path d="M0 300 C140 250 300 215 430 205 L430 250 C300 270 150 320 0 380 Z" fill="var(--brand-lavender)"/>
      <path d="M30 390 C80 320 260 250 430 238 L430 420 C300 425 150 440 60 470 C20 460 10 420 30 390 Z" fill="url(#photoBack)" role="img" aria-label="Photo of a gloved dental technician adjusting a dental articulator in the lab"/>
      <path d="M0 455 C150 430 300 405 430 398 L430 560 L0 560 Z" fill="var(--brand-blue)"/>
      <path d="M0 465 C150 440 300 414 430 407" stroke="#fff" stroke-width="2" fill="none"/>
    </svg>
    <div class="quote">
      <div class="quote__mark">&ldquo;</div>
      <p class="quote__text">Dana And Eli have always done a great job for our practice and our patients. Always willing to come through in a pinch too.</p>
      <p class="quote__author">Marcus T, Fairview, Va</p>
    </div>
    <div class="back-footer">
      <div class="wordmark wordmark--white">BRIGHT MEADOW<br>DENTAL LAB</div>
      <span class="back-footer__divider"></span>
      <div class="contact">
        <div class="contact__name">BRIGHT MEADOW DENTAL LAB</div>
        4126 Larkspur Ln, Suite 310, Larkton, VA 22190.<br>
        Office No: 703-555-0142 &nbsp;|&nbsp; Fax No: 703-555-0143<br>
        Email: info@bmdentalstudio.example
      </div>
    </div>
  </div>

  <div class="page page--front">
    <svg class="page-art" viewBox="0 0 430 560">
      <defs>
        <linearGradient id="photoFront" x1="0" y1="0" x2="1" y2="1">
          <stop offset="0" stop-color="#dfe2e6"/>
          <stop offset=".5" stop-color="#b7c3cf"/>
          <stop offset="1" stop-color="#6d8fb8"/>
        </linearGradient>
      </defs>
      <path d="M0 175 L330 175 C440 180 445 250 385 295 C320 345 170 385 0 415 Z" fill="var(--brand-lavender)"/>
      <path d="M0 195 L320 195 C410 198 415 255 360 295 C300 338 160 375 0 405 Z" fill="url(#photoFront)" role="img" aria-label="Photo of a dental technician working on a model set in an articulator"/>
      <path d="M0 420 C170 385 330 345 395 290 C370 340 220 395 0 440 Z" fill="var(--brand-blue)"/>
    </svg>
    <div class="wordmark wordmark--front"><span class="dot"></span>BRIGHT MEADOW<br><span class="wordmark__line2">DENTAL LAB</span></div>
    <div class="title">
      <div class="title__main">PRESENTATION</div>
      <div class="title__sub">FOLDER DESIGN</div>
    </div>
    <div class="url-tab">WWW.BMDENTALSTUDIO.EXAMPLE</div>
    <div class="front-baseline"></div>
  </div>
</section>

<section class="spread spread--inside">
  <div class="page page--inside-left">
    <svg class="page-art" viewBox="0 0 430 560">
      <circle cx="190" cy="470" r="100" fill="var(--disc-teal)"/>
      <circle cx="190" cy="470" r="26" fill="#9fa6dc"/>
      <circle cx="190" cy="470" r="10" fill="#5f68b8"/>
      <path d="M0 450 C120 446 240 440 300 430 L410 424 Q428 424 428 440 L430 560 L0 560 Z" fill="var(--brand-blue)"/>
    </svg>
    <div class="disc-label wordmark wordmark--white">BRIGHT MEADOW<br>DENTAL LAB</div>
    <div class="wordmark wordmark--inside-left"><span class="dot"></span>BRIGHT MEADOW<br><span class="wordmark__line2">DENTAL LAB</span></div>
  </div>

  <div class="page page--inside-right">
    <svg class="page-art" viewBox="0 0 430 560">
      <path d="M0 410 C0 395 8 388 22 386 L430 370 L430 560 L0 560 Z" fill="var(--brand-blue)"/>
    </svg>
    <div class="wordmark wordmark--inside-right"><span class="dot"></span>BRIGHT MEADOW<br><span class="wordmark__line2">DENTAL LAB</span></div>
    <div class="business-card">
      <div class="wordmark wordmark--white">BRIGHT MEADOW<br>DENTAL LAB</div>
      <div class="contact">
        <div class="contact__name">BRIGHT MEADOW DENTAL LAB</div>
        4126 Larkspur Ln, Suite 310, Larkton, VA 22190.<br>
        Office No: 703-555-0142 | Fax No: 703-555-0143<br>
        Email: info@bmdentalstudio.example
      </div>
    </div>
  </div>
</section>

</body>
</html>
```